Handout postcard for tradeshow

Please create a 2-sided handout postcard for use at a tradeshow. Card should be 4.25" x 5.5"

While postcard sized, a postcard with a place for an address/stamp is not wanted. We want a small handout for a tradeshow for people to take home with them.

The first side should emphasize cost savings.
The second side should emphasize environmental benefits.

The card's design doesn't need to match, but should be in line with the included poster design which will also be used at the tradeshow.

Possible graphics to include are listed below as well as the poster it should emulate.

```html
<!DOCTYPE html>
<html lang="en">
<head>
<meta charset="utf-8">
<title>ParcelWay – Tradeshow Handout</title>
<link rel="stylesheet" href="https://fonts.googleapis.com/css2?family=Open+Sans:ital,wght@0,400;0,600;0,700;1,700&display=swap">
<style>
  :root{
    --blue:#29a8e0;
    --blue-light:#45bfe9;
    --green:#3bb04a;
    --grey:#6d6e71;
    --ink:#231f20;
    --white:#ffffff;
    --stage:#ececec;
  }
  *{box-sizing:border-box;margin:0;padding:0}
  html,body{width:869px;height:1200px;overflow:hidden}
  body{background:var(--stage);font-family:"Open Sans",Arial,sans-serif;position:relative}

  .card{position:absolute;left:116px;width:638px;height:493px;background:var(--white);overflow:hidden;box-shadow:0 3px 10px rgba(0,0,0,.18)}
  .card--savings{top:84px}
  .card--green{top:650px}

  /* brand */
  .brand{position:absolute;z-index:3;display:flex;align-items:center;gap:8px;font-weight:700;letter-spacing:-1px;line-height:1}
  .brand__dot{border-radius:50%;flex:none}
  .card--savings .brand{left:20px;top:50px;font-size:48px;color:var(--grey)}
  .card--savings .brand__dot{width:40px;height:40px;background:var(--blue)}
  .card--green .brand{right:24px;top:44px;font-size:42px;color:var(--white)}
  .card--green .brand__dot{width:36px;height:36px;background:var(--white)}

  /* photo placeholders */
  .photo{position:absolute}
  .photo--city{left:0;top:0;width:638px;height:440px;
    clip-path:polygon(420px 0,638px 0,638px 440px,240px 440px);
    background:linear-gradient(180deg,#2b4a70 0%,#5d7894 35%,#3b3d46 58%,#7a3b33 82%,#b25a3a 100%)}
  .photo--forest{left:0;top:137px;width:638px;height:303px;
    background:radial-gradient(ellipse at 60% 45%,#4f7d45 0%,#2f5a32 45%,#1f3f26 100%)}

  /* card 1 blue panel */
  .panel{position:absolute;left:0;top:137px;width:440px;height:293px;
    clip-path:polygon(0 0,330px 0,430px 293px,0 293px);background:var(--blue);color:var(--white)}
  .panel__kicker{position:absolute;left:0;top:0;width:100%;height:35px;background:var(--blue-light);
    font-size:16.5px;padding:6px 0 0 22px}
  .panel__headline{position:absolute;left:0;top:35px;width:372px;height:75px;background:var(--green);
    clip-path:polygon(0 0,346px 0,372px 75px,0 75px);
    font-size:21.5px;line-height:1.25;padding:7px 0 0 22px;text-transform:uppercase;font-weight:400}
  .panel__lead{position:absolute;left:22px;top:118px;width:300px;font-size:10.5px;line-height:1.4;font-style:italic;font-weight:700}
  .panel__body{position:absolute;left:22px;top:160px;width:310px;font-size:9.6px;line-height:1.42}
  .panel__claim{position:absolute;left:0;top:223px;width:100%;height:70px;background:var(--blue-light);
    padding:8px 0 0 22px;line-height:1.2}
  .panel__claim-small{font-size:15px;display:block}
  .panel__claim-big{font-size:20.5px;display:block}

  /* badge */
  .badge{position:absolute;z-index:4;width:146px;height:146px;border-radius:50%;background:var(--green);border:3px solid var(--white);
    color:var(--white);text-align:center;display:flex;flex-direction:column;justify-content:center;align-items:center}
  .card--savings .badge{left:468px;top:331px}
  .card--green .badge{left:468px;top:310px}
  .badge__intro{font-size:7.5px}
  .badge__figure{font-size:17.5px;line-height:1.1}
  .badge__label{font-size:7.5px;font-weight:700;text-transform:uppercase}
  .badge__rule{width:94px;height:1px;background:var(--white);margin:6px 0 4px}

  /* contacts */
  .contacts{position:absolute;z-index:2;left:0;bottom:0;width:100%;height:53px;display:flex;align-items:center;gap:32px;padding-left:20px;font-size:14px}
  .card--savings .contacts{color:var(--grey)}
  .card--green .contacts{background:var(--blue);color:var(--white)}
  .contacts__item{display:flex;align-items:center;gap:10px}
  .contacts__item svg{width:22px;height:22px;fill:none;stroke:currentColor;stroke-width:1.5}

  /* card 2 */
  .sky{position:absolute;left:0;top:0;width:638px;height:440px;background:var(--blue)}
  .intro{position:absolute;left:0;top:0;width:638px;height:440px;background:var(--white);
    clip-path:polygon(0 0,291px 0,384px 183px,335px 440px,0 440px)}
  .intro__lead{position:absolute;left:22px;top:16px;color:var(--ink);font-size:25px;font-weight:400;line-height:1.2}
  .intro__title{position:absolute;left:22px;top:50px;color:var(--green);font-size:31px;font-weight:400;line-height:1.08}
  .feature{position:absolute;left:20px;display:flex;gap:12px}
  .feature--savings{top:143px}
  .feature--cheap{top:232px}
  .feature--validate{top:336px}
  .feature__icon{flex:none;width:38px;height:38px;border-radius:7px;background:var(--green);display:flex;align-items:center;justify-content:center}
  .feature__icon svg{width:24px;height:24px;fill:none;stroke:var(--white);stroke-width:1.6;stroke-linejoin:round;stroke-linecap:round}
  .feature__title{color:var(--green);font-size:13.5px;font-weight:400;line-height:1.2;margin-bottom:2px}
  .feature__text{color:var(--ink);font-size:9.8px;line-height:1.4}
  .feature--savings .feature__body{width:296px}
  .feature--cheap .feature__body{width:262px}
  .feature--validate .feature__body{width:232px}
</style>
</head>
<body>

<section class="card card--savings">
  <div class="photo photo--city" role="img" aria-label="City skyline at dusk with light trails on a highway"></div>
  <div class="brand"><span class="brand__dot"></span>ParcelWay</div>

  <div class="panel">
    <div class="panel__kicker">Cut your parcel costs by 10-50%</div>
    <h1 class="panel__headline">How much can<br>green parcels save me?</h1>
    <p class="panel__lead">Contact us to back-test your parcel data and see how much you could be saving on parcel costs.</p>
    <p class="panel__body">Our mission is to take the waste out of shipping. Every carrier drives every street in the US daily duplicating each others' routes. We help consolidate routes across carriers using our real-time bidding system for parcels.</p>
    <p class="panel__claim">
      <span class="panel__claim-small">ParcelWay Cuts the Waste out of Parcel Shipping &amp;</span>
      <span class="panel__claim-big">Reduces Costs by 10-50%</span>
    </p>
  </div>

  <footer class="contacts">
    <span class="contacts__item"><svg viewBox="0 0 24 24"><circle cx="12" cy="12" r="10"/><ellipse cx="12" cy="12" rx="4.5" ry="10"/><path d="M2 12h20M4 7h16M4 17h16"/></svg>www.ParcelWay.com</span>
    <span class="contacts__item"><svg viewBox="0 0 24 24"><rect x="2" y="5" width="20" height="14"/><path d="M2 5l10 8 10-8"/></svg>info@ParcelWay.com</span>
  </footer>

  <div class="badge">
    <span class="badge__intro">Send your Parcels Using:</span>
    <span class="badge__figure">40% Less</span>
    <span class="badge__label">Carbon Emissions</span>
    <span class="badge__rule"></span>
    <span class="badge__figure">25% Less</span>
    <span class="badge__label">Trucks on the Road</span>
  </div>
</section>

<section class="card card--green">
  <div class="sky"></div>
  <div class="photo photo--forest" role="img" aria-label="Aerial view of a road winding through a green forest"></div>

  <div class="intro">
    <p class="intro__lead">Join the</p>
    <h2 class="intro__title">GREEN PARCEL<br>MOVEMENT</h2>

    <div class="feature feature--savings">
      <span class="feature__icon"><svg viewBox="0 0 24 24"><circle cx="13" cy="8" r="5"/><path d="M13 5.5v5M11.5 7h2.5M12 9h2.5"/><path d="M2 17h4l4 2h6l5-4"/></svg></span>
      <div class="feature__body">
        <h3 class="feature__title">Easy, Risk-free Savings</h3>
        <p class="feature__text">Put your shipments up for bid via ParcelWay's simple API integration and receive a response in less than a second. You only use our real-time rates when we beat your contracted rate. No downside. No commitments necessary</p>
      </div>
    </div>

    <div class="feature feature--cheap">
      <span class="feature__icon"><svg viewBox="0 0 24 24"><rect x="4" y="4" width="16" height="8"/><rect x="4" y="12" width="8" height="8"/><rect x="12" y="12" width="8" height="8"/></svg></span>
      <div class="feature__body">
        <h3 class="feature__title">A Green Parcel is a Cheap Parcel</h3>
        <p class="feature__text">When a carrier is already serving an address, they can underbid other carriers for the next package, since they have already paid for that stop. This lowers shipping costs, reduces the number of duplicate stops, and cuts carbon emissions.</p>
      </div>
    </div>

    <div class="feature feature--validate">
      <span class="feature__icon"><svg viewBox="0 0 24 24"><path d="M2 6h12v11H2zM14 10h4l4 4v3h-8z"/><circle cx="6" cy="18" r="2"/><circle cx="18" cy="18" r="2"/><path d="M5 11l2 2 4-4"/></svg></span>
      <div class="feature__body">
        <h3 class="feature__title">Quickly Validate Savings</h3>
        <p class="feature__text">Connect with us to run a back-test on your shipping data, and see exactly how much money you would've saved on each parcel if you'd used ParcelWay for the past 3 months.</p>
      </div>
    </div>
  </div>

  <div class="brand"><span class="brand__dot"></span>ParcelWay</div>

  <footer class="contacts">
    <span class="contacts__item"><svg viewBox="0 0 24 24"><circle cx="12" cy="12" r="10"/><ellipse cx="12" cy="12" rx="4.5" ry="10"/><path d="M2 12h20M4 7h16M4 17h16"/></svg>www.ParcelWay.com</span>
    <span class="contacts__item"><svg viewBox="0 0 24 24"><rect x="2" y="5" width="20" height="14"/><path d="M2 5l10 8 10-8"/></svg>info@ParcelWay.com</span>
  </footer>

  <div class="badge">
    <span class="badge__intro">Send your Parcels Using:</span>
    <span class="badge__figure">40% Less</span>
    <span class="badge__label">Carbon Emissions</span>
    <span class="badge__rule"></span>
    <span class="badge__figure">25% Less</span>
    <span class="badge__label">Trucks on the Road</span>
  </div>
</section>

</body>
</html>
```